" A BHU (Blue Harbor Union) International Co. Consultoria & Negócios em Comércio Exterior atua nas áreas de importaçao e exportaçao. Oferecemos projetos customizados direcionados para a seleçao de fornecedores asiáticos. Além disso, representamos e apoiamos produtores em busca de expandir suas vendas para o mercado asiático. "

```html
<!DOCTYPE html>
<html lang="pt-BR">
<head>
<meta charset="utf-8">
<title>BHU International – Empresa</title>
<link rel="stylesheet" href="https://fonts.googleapis.com/css2?family=Arimo:wght@400;700&family=Roboto+Condensed:ital,wght@0,700;1,700&family=Open+Sans:wght@300;400&display=swap">
<style>
:root{
  --navy:#1b2b5e;
  --navy-dark:#14214a;
  --orange:#e2891d;
  --page:#ffffff;
  --bg:#f1f1f1;
  --card:#e8e8e8;
  --text:#5a5a5a;
  --muted:#8c8c8c;
  --nav:#e9e9e9;
}
*{box-sizing:border-box;margin:0;padding:0}
html,body{width:1200px;height:1200px;overflow:hidden}
body{background:var(--bg);font-family:"Arimo",Arial,sans-serif;color:var(--text);position:relative}
.page{position:absolute;left:48px;top:0;width:1104px;height:1200px;background:var(--page)}
.abs{position:absolute}

.brand{left:180px;top:38px;display:flex;align-items:center;gap:16px}
.brand-mark{width:58px;height:58px;border-radius:50%;background:var(--navy)}
.brand-name{font-family:"Roboto Condensed",sans-serif;font-weight:700;font-size:62px;color:var(--navy);line-height:1}
.brand-tag{left:180px;top:130px;font-size:11px;font-weight:700;color:var(--navy)}

.flags{left:916px;top:24px;display:flex;gap:10px}
.flags span{width:26px;height:16px;background:#b7b7b7}
.flags span:first-child{background:#3a9b4a}
.flags span:nth-child(2){background:#6b7fa6}

.slogan{left:740px;top:96px;font-family:"Roboto Condensed",sans-serif;font-style:italic;font-weight:700;font-size:25px;color:var(--navy)}
.search{left:870px;top:180px;width:178px;height:14px;background:#ececec;border-radius:2px}

.nav{left:173px;top:172px;width:875px;height:44px;background:linear-gradient(#f6f6f6,var(--nav));display:flex}
.nav a{display:block;padding:0 26px;line-height:44px;font-size:14px;color:var(--muted);text-decoration:none;border-right:1px solid #d4d4d4}
.nav a.active{background:var(--orange);color:#fff;font-weight:700}
.subnav{left:272px;top:216px;height:36px;background:var(--orange);display:flex;z-index:1}
.subnav a{display:block;padding:0 14px;line-height:36px;font-size:13px;font-weight:700;color:#fff;text-decoration:none}
.subnav a.active{background:var(--navy-dark)}

.hero{left:173px;top:216px;width:875px;height:180px;background:linear-gradient(100deg,#2b66b8 0%,#3d89d4 45%,#9cc6ea 68%,#2a5fa8 100%);z-index:0}

.section-bar{left:173px;top:396px;width:875px;height:55px;background:var(--navy);display:flex;align-items:center;padding-left:12px;gap:14px}
.section-bar h1{font-family:"Roboto Condensed",sans-serif;font-weight:700;font-size:28px;color:#cfd4e2;text-transform:uppercase}
.section-bar span{border-left:1px solid #fff;padding-left:14px;font-size:12px;font-weight:700;color:#fff}

.card{top:468px;width:206px;height:336px;background:var(--card);text-align:center;padding:16px 14px}
.card h2{font-family:"Roboto Condensed",sans-serif;font-weight:700;font-size:18px;color:var(--navy);text-transform:uppercase;padding-bottom:10px;border-bottom:1px solid #cfcfcf;margin-bottom:22px}
.card p{font-size:12px;line-height:15px;color:var(--text);text-transform:uppercase}
.card ul{list-style:none;font-size:12px;text-transform:uppercase;line-height:27px}

.footer{left:0;top:912px;width:1104px;height:288px;background:#f0f0f0}
.footer h3{font-family:"Open Sans",sans-serif;font-weight:300;font-size:26px;line-height:36px;color:var(--orange)}
.sitemap{left:125px;top:18px}
.sitemap ul{list-style:none;margin-top:10px;font-size:12px;line-height:16px;color:var(--muted);text-transform:uppercase}
.contact{left:497px;top:18px;border-left:1px solid #d6d6d6;padding-left:12px;height:180px}
.contact ul{list-style:none;margin-top:10px;font-size:12px;line-height:16px;color:var(--muted)}
.contact li{display:flex;align-items:center;gap:8px}
.contact address{font-style:normal;margin-top:14px;font-size:12px;line-height:16px;color:var(--muted)}
.social{left:900px;top:20px;display:flex;gap:14px}
.social span{width:26px;height:40px;background:var(--navy);border-radius:2px}
.social span:nth-child(2){background:#3a8fc4}
.social span:nth-child(3){background:#4a78a8}
.foot-brand{left:840px;top:120px;display:flex;align-items:center;gap:10px}
.foot-brand i{width:28px;height:28px;border-radius:50%;background:#c9ccd4}
.foot-brand b{font-family:"Roboto Condensed",sans-serif;font-size:40px;color:#b9bcc6}
.foot-line{left:125px;top:210px;width:925px;height:6px;background:var(--navy)}
.copyright{left:125px;top:227px;font-size:12px;color:var(--muted)}
.copyright b{color:var(--navy)}
.foot-search{left:790px;top:224px;width:258px;height:20px;display:flex;align-items:center;justify-content:space-between;font-size:11px;color:#aaa;padding-left:8px}
.foot-search strong{color:var(--orange)}
</style>
</head>
<body>
<div class="page">
  <header>
    <div class="abs brand"><span class="brand-mark"></span><span class="brand-name">BHU</span></div>
    <div class="abs brand-tag">Consultoria &amp; Negócios em Comércio Exterior</div>
    <div class="abs flags"><span></span><span></span><span></span><span></span></div>
    <div class="abs slogan">ROMPENDO FRONTEIRAS</div>
    <div class="abs search"></div>
  </header>

  <nav class="abs nav">
    <a href="#">Home</a><a href="#" class="active">Empresa</a><a href="#">Serviços</a><a href="#">Contatos</a><a href="#">Trabalhe Conosco</a>
  </nav>
  <div class="abs hero" role="img" aria-label="Mão segurando um globo de vidro sobre fundo azul"></div>
  <div class="abs subnav"><a href="#" class="active">Nossos Ideais</a><a href="#">Nosso Time</a><a href="#">Mercados</a></div>

  <div class="abs section-bar"><h1>Empresa</h1><span>NOSSOS IDEAIS</span></div>

  <section class="abs card" style="left:173px">
    <h2>Essência</h2>
    <p>A BHU International tem como propósito romper fronteiras comerciais, potencializando negócios com o continente asiático.</p>
  </section>
  <section class="abs card" style="left:396px">
    <h2>Missão</h2>
    <p>Desenvolver soluções em comércio exterior que proporcionem a nossos clientes a conquista de novos mercados e a construção de alianças sólidas.</p>
  </section>
  <section class="abs card" style="left:619px">
    <h2>Visão</h2>
    <p>Ser reconhecida nacionalmente e internacionalmente como referência em soluções de comércio exterior nos negócios com a Ásia.</p>
  </section>
  <section class="abs card" style="left:845px">
    <h2>Valores</h2>
    <ul><li>Excelência</li><li>Honestidade</li><li>Ética</li><li>Determinação</li><li>Meritocracia</li></ul>
  </section>

  <footer class="abs footer">
    <div class="abs sitemap">
      <h3>Mapa do Site</h3>
      <ul><li>Home</li><li>Empresa</li><li>Serviços</li><li>Contatos</li><li>Trabalhe Conosco</li><li>O Século da Ásia</li><li>Presença na Ásia</li><li>Controle de Qualidade</li></ul>
    </div>
    <div class="abs contact">
      <h3>Contato</h3>
      <ul>
        <li><svg width="12" height="12" viewBox="0 0 12 12"><path d="M2 1h3l1 3-2 1a7 7 0 0 0 3 3l1-2 3 1v3c-6 0-9-3-9-9z" fill="#8c8c8c"/></svg>+55 (31) 4000-0000 (Brasil)</li>
        <li><svg width="12" height="12" viewBox="0 0 12 12"><path d="M2 1h3l1 3-2 1a7 7 0 0 0 3 3l1-2 3 1v3c-6 0-9-3-9-9z" fill="#8c8c8c"/></svg>+ (86) 100-0000-0000 (China)</li>
        <li><svg width="12" height="12" viewBox="0 0 12 12"><rect x="1" y="2.5" width="10" height="7" fill="none" stroke="#8c8c8c"/><path d="M1 3l5 4 5-4" fill="none" stroke="#8c8c8c"/></svg>contato@bhuinternational.com.br</li>
      </ul>
      <address>Rua das Marés, 120, Sala 305<br>Bairro Porto Azul<br>Cep: 30.000-000<br>Vila Serena-MG</address>
    </div>
    <div class="abs social"><span></span><span></span><span></span></div>
    <div class="abs foot-brand"><i></i><b>BHU</b></div>
    <div class="abs foot-line"></div>
    <div class="abs copyright">Todos os Direitos Reservados - Desenvolvido por <b>Onda Digital</b></div>
    <div class="abs foot-search">Buscar no site <strong>OK</strong></div>
  </footer>
</div>
</body>
</html>
```